Prospective Client Marketing Power Point Refresh/Update

My company has been using the attached power point to share with prospective clients. I'd like to have it refreshed with new graphics and style. The color pallet is something we'd like to stay true to. We are looking for your design expertise and ideas to help us update the look of the PP. We work with high wealth clients and want to have this reflect the value we can bring to the table.

Target Market(s)

Wealth Management Clients

Industry/Entity Type

Financial Advisors

Font styles to use
Sans Serif

Colors
0054AA
0677BA
7BADD7
CADEEF
E8F1F8
0094D4
00A9DD
6FCCEA
C7EBF8
E9F6FB

Requirements
Must have
• Updated look
Nice to have
• Fresh graphics

```html
<!DOCTYPE html>
<html lang="en">
<head>
<meta charset="utf-8">
<title>Wealth Planning Presentation Slides</title>
<link href="https://fonts.googleapis.com/css2?family=Poppins:wght@300;400;500;600;700&display=swap" rel="stylesheet">
<style>
  :root{
    --navy:#0054AA;
    --blue:#0677BA;
    --sky:#7BADD7;
    --ice:#CADEEF;
    --mist:#E8F1F8;
    --cyan:#0094D4;
    --teal:#2A95B8;
    --aqua:#6FCCEA;
    --green:#8CC63F;
    --leaf:#7DB33A;
    --lime:#B0CB5F;
    --ink:#222428;
    --grey:#666a70;
    --card:#EFF0F2;
    --stage:#E8EAEE;
  }
  *{margin:0;padding:0;box-sizing:border-box}
  html,body{width:1200px;height:867px;overflow:hidden}
  body{background:var(--stage);font-family:'Poppins',sans-serif;color:var(--ink);position:relative}
  .slide{position:absolute;width:514px;height:364px;background:#fff;overflow:hidden;box-shadow:0 6px 14px rgba(0,0,0,.12)}
  .s-markets{left:68px;top:53px}
  .s-behavior{left:618px;top:53px}
  .s-plan{left:68px;top:450px}
  .s-execute{left:618px;top:450px}
  .abs{position:absolute}
  .tab{position:absolute;left:-48px;width:70px;height:70px;border-radius:50%;background:var(--blue)}
  .headline{position:absolute;font-size:19.5px;line-height:23px;font-weight:400;color:var(--ink)}
  .headline b{color:var(--blue);font-weight:700}
  .h-sub{font-size:8.6px;font-weight:600;color:var(--blue);line-height:11px}
  .body{font-size:7.3px;line-height:8.8px;color:var(--ink)}
  .justify{text-align:justify}

  /* markets */
  .chart{position:absolute;left:27px;top:146px;width:205px;height:120px}
  .dims{position:absolute;left:0;top:0;width:514px;height:364px}
  .dim-label{font-size:4.8px;line-height:6px;color:var(--ink)}
  .dim-label b{font-weight:600}
  .classes{position:absolute;left:273px;top:266px;width:120px;display:grid;grid-template-columns:57px 63px;row-gap:6px;font-size:5.2px;line-height:6px}
  .classes span{position:relative;padding-left:6px}
  .classes span::before{content:"";position:absolute;left:0;top:1.5px;width:3px;height:3px;border-radius:50%;background:var(--dot,#7DB33A)}
  .classes .g{--dot:var(--leaf)}
  .classes .b{--dot:var(--aqua)}
  .classes .d{--dot:#444}
  .classes .l{--dot:#bbb}
  .returns-grid{position:absolute;left:402px;top:268px;width:88px;height:70px;background:linear-gradient(135deg,#5a6068,#2aa0c8 35%,#9ccbe0 55%,#7DB33A 75%,#c4c8cc)}
  .years{position:absolute;left:402px;top:262px;width:88px;display:flex;justify-content:space-between;font-size:2.6px;color:var(--ink)}

  /* behavior */
  .bcard{position:absolute;top:110px;width:151px;height:112px;background:var(--card);border-radius:8px;padding:9px 8px}
  .bcard .h-sub{margin-bottom:2px}
  .bcard .green{color:var(--green)}
  .tags{position:absolute;left:210px;top:243px;width:110px;height:66px}
  .tag{position:absolute;height:8.5px;background:#e7e9eb;font-size:4.6px;line-height:8.5px;text-align:center;font-weight:500}
  .t-g{color:var(--leaf)} .t-b{color:var(--blue)} .t-d{color:#555}
  .checks{position:absolute;left:343px;top:236px;width:160px;list-style:none;font-size:5.9px;line-height:7px}
  .checks li{position:relative;padding-left:7px;margin-bottom:7.6px}
  .checks li::before{content:"›";position:absolute;left:0;top:-0.5px}

  /* plan */
  .plan-field{position:absolute;left:69px;top:0;width:445px;height:364px;background:var(--lime)}
  .plan-title{position:absolute;left:33px;top:180px;transform:translate(-50%,-50%) rotate(-90deg);white-space:nowrap;font-size:28px;font-weight:400;color:var(--ink);line-height:30px}
  .plan-title b{color:var(--lime);font-weight:600}
  .pcard{position:absolute;width:132px;height:147px;background:#F1F2F2;border-radius:5px;padding:8px 10px}
  .pcard svg{width:24px;height:24px;display:block;margin-bottom:5px}
  .ptitle{font-size:9.4px;line-height:11px;color:var(--teal);letter-spacing:.1px}
  .ptitle b{font-weight:600}
  .psub{font-size:7.4px;line-height:8.7px;font-weight:600;color:var(--blue);margin:4px 0 9px}
  .plist{list-style:none;font-size:6.1px;line-height:7.3px}
  .plist li{position:relative;padding-left:7px}
  .plist li::before{content:"›";position:absolute;left:0}
  .pnote{font-size:6.1px;line-height:7.3px;margin-top:6px}
  .c1{left:87px} .c2{left:226px} .c3{left:364px}
  .r1{top:27px} .r2{top:180px}

  /* execute */
  .phones{position:absolute;left:41px;top:87px;width:196px;height:243px;border-radius:14px;background:linear-gradient(160deg,#3a3d42,#dfe6ec 40%,#37a6c8 62%,#7DB33A 85%,#f4f6f8)}
  .site-title{position:absolute;left:276px;top:102px;font-size:17.5px;line-height:18.5px;font-weight:700;color:var(--leaf);letter-spacing:.3px}
  .site-sub{position:absolute;left:276px;top:150px;font-size:10px;font-weight:600;color:var(--blue)}
  .site-body{position:absolute;left:276px;top:172px;width:220px;font-size:9.3px;line-height:11.7px;color:var(--ink)}
  .site-body p+p{margin-top:12px}
</style>
</head>
<body>

<!-- Slide: Efficient markets -->
<section class="slide s-markets">
  <div class="tab" style="top:10px"></div>
  <h1 class="headline" style="left:27px;top:19px;font-size:22px;line-height:24px">The power of<br><b>Efficient</b> Markets</h1>

  <h2 class="h-sub abs" style="left:27px;top:83px">Let Markets Work for you</h2>
  <p class="body abs" style="left:27px;top:95px;width:215px">The financial markets have rewarded long-term investors. People expect a positive return on the capital they supply, &amp; historically, the equity and bond markets have provided growth of wealth that has more then offset inflation.</p>

  <svg class="chart" viewBox="0 0 205 120" role="img" aria-label="Growth of a dollar line chart, 1926 to 2018">
    <text x="0" y="6" font-size="4.3" fill="#222">Growth of a Dollar, 1926 - 2018</text>
    <text x="0" y="11" font-size="4.3" fill="#222">(compounded monthly)</text>
    <g font-size="2.8" fill="#222">
      <circle cx="3" cy="21" r="2.8" fill="#1f8fb8"/><text x="8" y="20" font-weight="600">$20,445</text><text x="8" y="23">US small cap</text>
      <circle cx="3" cy="34" r="2.8" fill="#8fd0e2"/><text x="8" y="33" font-weight="600">$7,025</text><text x="8" y="36">US large cap</text>
      <circle cx="3" cy="47" r="2.8" fill="#7ab53b"/><text x="8" y="46" font-weight="600">$142</text><text x="8" y="49">US Long term</text><text x="8" y="51.5">Government bonds</text>
      <circle cx="53" cy="21" r="2.8" fill="#b5d44d"/><text x="58" y="20" font-weight="600">$21</text><text x="58" y="23">US Treasury Bills</text>
      <circle cx="53" cy="34" r="2.8" fill="#555"/><text x="58" y="33" font-weight="600">$21</text><text x="58" y="36">US Inflation</text>
    </g>
    <line x1="2" y1="110" x2="205" y2="110" stroke="#ddd" stroke-width=".5"/>
    <line x1="204" y1="0" x2="204" y2="110" stroke="#ddd" stroke-width=".5"/>
    <g fill="none" stroke-width="1" stroke-linejoin="round">
      <polyline stroke="#666" points="3,95 30,94 70,90 100,85 130,80 160,74 196,70"/>
      <polyline stroke="#b5d44d" points="3,94 30,92 70,90 100,84 130,76 160,67 196,65"/>
      <polyline stroke="#7ab53b" points="3,93 20,92 40,90 70,88 90,82 110,76 130,70 150,60 170,52 196,50"/>
      <polyline stroke="#8fd0e2" points="3,90 10,86 20,87 35,80 50,74 70,66 90,56 110,50 130,40 150,34 170,24 196,12"/>
      <polyline stroke="#1f8fb8" points="3,92 9,96 13,105 17,87 25,89 35,78 45,72 60,70 80,58 100,50 120,40 140,33 160,26 180,18 196,7"/>
    </g>
    <g font-size="3" fill="#444">
      <text x="0" y="118">1926</text><text x="19" y="118">1936</text><text x="41" y="118">1946</text><text x="63" y="118">1956</text><text x="85" y="118">1966</text><text x="107" y="118">1976</text><text x="129" y="118">1986</text><text x="151" y="118">1996</text><text x="173" y="118">2006</text><text x="195" y="118">2016</text>
    </g>
  </svg>

  <h2 class="h-sub abs" style="left:27px;top:281px">Consider the Drivers of returns</h2>
  <p class="body abs" style="left:27px;top:293px;width:212px">There is a wealth of academic research into what drives returns. Expected returns depend on current market prices and expected future cash flows. Investors can use this information to pursue higher expected returns in their portfolios.</p>

  <h2 class="h-sub abs" style="left:273px;top:19px">Avoid Market Timing</h2>
  <p class="body justify abs" style="left:273px;top:31px;width:210px">You never know which market segments will out perform from year to year. By holding a globally diversified portfolio, investors are well positioned to seek returns wherever they occur.</p>

  <svg class="dims" viewBox="0 0 514 364" aria-hidden="true">
    <defs><filter id="soft" x="-30%" y="-30%" width="160%" height="160%"><feDropShadow dx="0" dy="1.5" stdDeviation="3" flood-opacity=".12"/></filter></defs>
    <circle cx="309" cy="129" r="33" fill="#fff" filter="url(#soft)"/>
    <line x1="338" y1="110" x2="354" y2="99" stroke="#222" stroke-width=".6"/>
    <line x1="338" y1="148" x2="354" y2="159" stroke="#222" stroke-width=".6"/>
    <circle cx="356" cy="98" r="4" fill="var(--aqua)" stroke="#fff" stroke-width="1.2"/>
    <circle cx="356" cy="160" r="4" fill="var(--aqua)" stroke="#fff" stroke-width="1.2"/>
    <circle cx="376" cy="87" r="13" fill="#fff" filter="url(#soft)"/>
    <circle cx="376" cy="87" r="10.5" fill="#2a95b8"/>
    <g stroke="#fff" stroke-width=".7" fill="none"><line x1="376" y1="81" x2="376" y2="93"/><line x1="370" y1="84" x2="382" y2="84"/><path d="M368 89 l2-5 2 5z M380 89 l2-5 2 5z"/><line x1="373" y1="93" x2="379" y2="93"/></g>
    <circle cx="376" cy="170" r="13" fill="#fff" filter="url(#soft)"/>
    <circle cx="376" cy="170" r="10.5" fill="var(--leaf)"/>
    <g stroke="#fff" stroke-width=".7" fill="none"><circle cx="377" cy="166" r="3"/><path d="M369 174 q4-3 7 0 l5-2"/></g>
    <text x="309" y="127" font-size="5.6" font-weight="600" text-anchor="middle" fill="#222" font-family="Poppins,sans-serif">Dimensions</text>
    <text x="309" y="134" font-size="5.6" font-weight="600" text-anchor="middle" fill="#222" font-family="Poppins,sans-serif">of Expected</text>
    <text x="309" y="141" font-size="5.6" font-weight="600" text-anchor="middle" fill="#222" font-family="Poppins,sans-serif">Returns</text>
  </svg>
  <p class="dim-label abs" style="left:392px;top:71px;width:118px"><b>Equities</b><br>Company Size (Market Capitalization)<br>Relative Price (Price/Book Equity)<br>Profitability (Operating Profits/Book Equity)</p>
  <p class="dim-label abs" style="left:394px;top:157px;width:116px"><b>Fixed Income</b><br>Term (Sensitivity to Interest Rates)<br>Credit (Credit quality of Issuer)<br>Currency (Currency of Issuance)</p>

  <h2 class="h-sub abs" style="left:273px;top:209px">Practice Smart Diversification</h2>
  <p class="body justify abs" style="left:273px;top:222px;width:210px">Holding securities across many market segments can help manage overall risk. But diversifying within your home market may not be enough. Global diversification can broaden your investment universe.</p>

  <div class="classes">
    <span class="b">Us Large Cap</span><span class="l">Intl.Large Cap Value</span>
    <span class="b">Us Large Cap Value</span><span class="l">Intl. Small Cap Value</span>
    <span class="g">Us Small Cap</span><span class="l">Emerging Markets</span>
    <span class="g">Us Small Cap Value</span><span class="l">Five Years US Govt.Fixed</span>
    <span class="d">US Real Estate</span>
  </div>
  <div class="years"><span>2004</span><span>2006</span><span>2008</span><span>2010</span><span>2012</span><span>2014</span><span>2016</span><span>2018</span></div>
  <div class="returns-grid" role="img" aria-label="Grid of yearly asset class return rankings in blue, green and grey squares"></div>
</section>

<!-- Slide: Behavioral finance -->
<section class="slide s-behavior">
  <div class="tab" style="top:29px"></div>
  <h1 class="headline" style="left:32px;top:41px">Behavioral Finance...<br><b>Beware of your emotions</b></h1>

  <div class="bcard" style="left:24px">
    <h2 class="h-sub">Manage Your Emotions</h2>
    <p class="body">Many people struggle to separate their emotions from investing. Markets go up and down. Reacting to current market conditions may lead to making poor investment decisions.</p>
  </div>
  <div class="bcard" style="left:181px">
    <h2 class="h-sub">Look Beyond the Headlines</h2>
    <p class="body">Daily market news and commentary can challenge your investment discipline. Some messages stir anxiety about the future while others tempt you to chase the latest investment fad. When headlines unsettle you, consider the source and maintain a long-term</p>
  </div>
  <div class="bcard" style="left:339px">
    <h2 class="h-sub green">Focus on What you Can Control</h2>
    <p class="body">A financial advisor can offer expertise and guidance to help you focus on actions that add value. This can lead to a better investment experience.</p>
  </div>

  <svg class="abs" style="left:0;top:0" width="200" height="364" viewBox="0 0 200 364" aria-label="Emotional cycle of investing">
    <polyline points="41,274 70,250 99,274 130,300 158,274" fill="none" stroke="#3a9cc4" stroke-width=".8"/>
    <g fill="#3a9cc4"><circle cx="41" cy="274" r="1.6"/><circle cx="70" cy="250" r="1.6"/><circle cx="99" cy="274" r="1.6"/><circle cx="130" cy="300" r="1.6"/><circle cx="158" cy="274" r="1.6"/></g>
    <g font-family="Poppins,sans-serif" font-size="5.4" fill="#7DB33A" text-anchor="middle">
      <text x="42" y="283">Optimism</text><text x="70" y="246">Elation</text><text x="99" y="270">Nervousness</text><text x="130" y="308">Fear</text><text x="158" y="270">Optimism</text>
    </g>
  </svg>

  <div class="tags">
    <div class="tag t-g" style="left:0;top:0;width:43px">RETIRE RICH</div>
    <div class="tag t-b" style="left:14px;top:10.5px;width:74px">SELL STOCKS NOW</div>
    <div class="tag t-d" style="left:0;top:21.5px;width:77px">THE LOOMING RECESSION</div>
    <div class="tag t-g" style="left:-6px;top:32.5px;width:106px">THE TOP 10 FUNDS TO OWN</div>
    <div class="tag t-b" style="left:10px;top:43.5px;width:100px">MARKET HITS RECORD HIGH</div>
    <div class="tag t-d" style="left:8px;top:55px;width:80px">HOUSING MARKET BOOM</div>
  </div>

  <ul class="checks">
    <li>Create an investment plan to fit your need &amp; risk tolerance</li>
    <li>Structure a portfolio along the dimensions of expected returns</li>
    <li>Diversity globally</li>
    <li>Manage expenses, turnover and taxes</li>
    <li>Stay disciplined through market dips &amp; swings</li>
  </ul>
</section>

<!-- Slide: Planning tools -->
<section class="slide s-plan">
  <div class="plan-field"></div>
  <h1 class="plan-title">Do you have a <b>Plan?</b></h1>

  <article class="pcard c1 r1">
    <svg viewBox="0 0 24 24" fill="none" stroke="#7DB33A" stroke-width=".9"><rect x="2" y="7" width="15" height="11" rx="1"/><line x1="1" y1="20" x2="18" y2="20"/><circle cx="9.5" cy="11" r="2"/><path d="M6 17c0-2 7-2 7 0"/><path d="M15 2h8v6h-4l-2 2V8h-2z"/></svg>
    <h3 class="ptitle"><b>DIGITAL</b>ADVICE</h3>
    <p class="psub">A planning first, Self Directed Platform</p>
    <ul class="plist"><li>Automated client journey</li><li>A gateway to brokeage execution</li><li>Umatched client experience</li><li>Side by side management of digital and fully advised clients</li><li>Co-developed with Northgate</li></ul>
  </article>

  <article class="pcard c2 r1">
    <svg viewBox="0 0 24 24" fill="none" stroke="#7DB33A" stroke-width=".9"><circle cx="10" cy="10" r="7"/><line x1="15" y1="15" x2="21" y2="21" stroke-width="2"/><polyline points="6,11 9,8 11,11 14,8"/></svg>
    <h3 class="ptitle"><b>NEEDS</b>ANALYSIS</h3>
    <p class="psub">Focused, Easy-to-Create Plans</p>
    <ul class="plist"><li>Modules for a variety of common planning concepts including:</li></ul>
    <p class="pnote">Assest allocation | Insurance | College Planning | Retirement | Income protection and more</p>
    <ul class="plist" style="margin-top:6px"><li>Create deliverables in minutes</li></ul>
  </article>

  <article class="pcard c3 r1">
    <svg viewBox="0 0 24 24" fill="none" stroke="#7DB33A" stroke-width=".9"><path d="M2 22h20M5 22v-5h4v5M10 22v-9h4v9M15 22V9h4v13"/><line x1="17" y1="9" x2="17" y2="2"/><path d="M17 2h5l-1.5 1.5L22 5h-5"/></svg>
    <h3 class="ptitle"><b>GOAL</b>PLANNER</h3>
    <p class="psub">Interactive Scenario Planning</p>
    <ul class="plist"><li>Compare up to four scenerios</li><li>Change values on the fly</li><li>Use Monte Carlo or straight-line math</li><li>Drive goal-focused conversations</li></ul>
  </article>

  <article class="pcard c1 r2">
    <svg viewBox="0 0 24 24" fill="none" stroke="#7DB33A" stroke-width=".9"><circle cx="7" cy="8" r="3"/><circle cx="17" cy="8" r="3"/><path d="M2 22c0-5 10-5 10 0M12 22c0-5 10-5 10 0"/><path d="M5 2l4 4M9 2L5 6"/><polyline points="15,3 17,5 20,1"/></svg>
    <h3 class="ptitle"><b>DECISION</b>CENTER</h3>
    <p class="psub">Interactive Cash Flow Planning</p>
    <ul class="plist"><li>Open any scenario to see lifetime cash flow</li><li>Demonstrate effects of important decisions</li><li>Use advance techniques and what-ifs</li><li>Collaboratively build a plan with your clients</li></ul>
  </article>

  <article class="pcard c2 r2">
    <svg viewBox="0 0 24 24" fill="none" stroke="#7DB33A" stroke-width=".9"><rect x="3" y="2" width="14" height="19" rx="1"/><polyline points="5,6 6.5,7.5 9,5"/><line x1="11" y1="6" x2="15" y2="6"/><polyline points="5,11 6.5,12.5 9,10"/><line x1="11" y1="11" x2="15" y2="11"/><line x1="11" y1="16" x2="15" y2="16"/><circle cx="19" cy="18" r="4"/></svg>
    <h3 class="ptitle"><b>ADVANCED</b>PLANNING</h3>
    <p class="psub">Complex and Advanced Techniques</p>
    <ul class="plist"><li>Model a wide range of financial scenarios</li><li>Create detailed retirement plans</li><li>Apply "what-if" scenarios to plans</li><li>Conduct In-depth investment analysis</li><li>Leverage comprehensive and flexible tax calculations</li></ul>
  </article>

  <article class="pcard c3 r2">
    <svg viewBox="0 0 24 24" fill="none" stroke="#7DB33A" stroke-width=".9"><path d="M12 8l4 2v4l-4 2-4-2v-4z"/><path d="M12 1v5M12 18v5M1 12h5M18 12h5M4 4l3.5 3.5M20 4l-3.5 3.5M4 20l3.5-3.5M20 20l-3.5-3.5"/></svg>
    <h3 class="ptitle"><b>DISTRIBUTION</b>CENTER</h3>
    <p class="psub">Interactive Estate Planning</p>
    <ul class="plist"><li>Visually tel the story of an estate plan</li><li>Show how planning techniques affect the estate</li><li>Cover topics like distributions and survivor income</li><li>Colaboratively create a distribution plan</li></ul>
  </article>
</section>

<!-- Slide: Client website -->
<section class="slide s-execute">
  <div class="tab" style="top:29px"></div>
  <h1 class="headline" style="left:31px;top:50px">Are you <b>executing</b> on it?</h1>

  <div class="phones" role="img" aria-label="Two smartphones showing the client portal with account list, net worth and investments panels"></div>

  <h2 class="site-title">YOUR PERSONAL<br>FINANCIAL WEBSITE</h2>
  <p class="site-sub">Take control of your financial world</p>
  <div class="site-body">
    <p>Your personal financial management website makes it easy to manage both your wealth and your well-being</p>
    <p>More than half of the world's Web traffic is now coming from mobile phones. You will have a consistent and unified experience across all devices – from a mobile phone, tablet, or personal computer – making it easier than ever to use the Client Portal from wherever you are.</p>
  </div>
</section>

</body>
</html>
```